Flyer-Design für  Ambulanten Pflegedienst
Flyer-Design für Ambulanten Pflegedienst
Zielgruppe
Ambulanter Pflegedienst, Versorgung von Alten und Kranken. Hauswirtschaftliche Unterstützung
Aufgabenstellung
Normaler Flyer, 3 Seiten,

```html
<!DOCTYPE html>
<html lang="de">
<head>
<meta charset="utf-8">
<title>Lindwerk Pflege Brandel – Flyer</title>
<link href="https://fonts.googleapis.com/css2?family=Montserrat:wght@400;500;700;800&display=swap" rel="stylesheet">
<style>
:root{
  --green:#5aab3c;
  --green-dark:#4a9a30;
  --green-light:#8cc63f;
  --brown:#7a4a35;
  --text:#6b4a3c;
  --paper:#ffffff;
  --stage:#f3f4f2;
}
*{box-sizing:border-box;margin:0;padding:0}
html,body{width:1200px;height:2182px;overflow:hidden;background:var(--stage);font-family:'Montserrat',sans-serif;color:var(--text)}
.canvas{position:relative;width:1200px;height:2182px}
.spread{position:absolute;left:30px;width:1140px;height:806px;display:flex;background:var(--paper);box-shadow:0 14px 40px rgba(0,0,0,.14)}
.spread--inside{top:200px}
.spread--outside{top:1176px}
.panel{position:relative;width:380px;height:806px;overflow:hidden;padding:0 34px}
.panel + .panel{border-left:1px solid #e6e8e4}
.deco{position:absolute;left:0;width:380px;pointer-events:none}
.deco--top{top:0}
.deco--bottom{bottom:0}
.band-label{position:absolute;top:14px;left:34px;color:#fff;font-weight:800;font-size:15px;letter-spacing:.5px;z-index:2}
.section{position:relative;z-index:2}
.kicker{display:block;text-align:center;font-size:10px;color:var(--text);margin-bottom:2px}
.heading{display:flex;align-items:center;gap:8px;color:var(--green);font-weight:800;font-size:17px;letter-spacing:.5px;text-transform:uppercase;margin-bottom:12px;white-space:nowrap}
.heading::before,.heading::after{content:"";flex:1;height:3px;background:var(--green);border-radius:2px}
.checklist{list-style:none}
.checklist li{position:relative;padding-left:22px;font-size:12.5px;line-height:1.35;margin-bottom:7px}
.checklist li::before{content:"";position:absolute;left:2px;top:2px;width:12px;height:12px;border:1.5px solid var(--green);border-radius:50%}
.checklist li::after{content:"";position:absolute;left:6px;top:5px;width:4px;height:7px;border:solid var(--green);border-width:0 2px 2px 0;transform:rotate(45deg)}
.photo{position:absolute;border-radius:50%;z-index:1}
.photo--pills{background:radial-gradient(circle at 40% 40%,#f4f1ee,#cfd8e3)}
.photo--hug{background:radial-gradient(circle at 60% 40%,#f1ece8,#b8b0aa)}
.photo--hair{background:radial-gradient(circle at 45% 45%,#efe6dc,#c9b9a6)}
.photo--wash{background:radial-gradient(circle at 50% 45%,#f3e2d6,#c7bfd9)}
.photo--duo{background:radial-gradient(circle at 50% 45%,#f2e6dd,#c9b3a3)}
.banner-text{position:absolute;z-index:3;color:#fff;font-weight:800;font-size:18px;letter-spacing:.8px;text-transform:uppercase}
.brand{text-align:center;color:var(--green);font-weight:800;font-size:27px;line-height:1.05;text-transform:uppercase;letter-spacing:.5px}
.brand-dot{display:block;width:46px;height:46px;border-radius:50%;background:var(--green);margin:0 auto 10px}
.brand-sub{display:block;font-size:19px;letter-spacing:3px}
.body-copy{font-size:12px;line-height:1.45;text-align:center}
.phone{display:flex;align-items:center;justify-content:center;gap:10px;color:var(--green);font-weight:800;font-size:26px;margin:14px 0}
.address{text-align:center;font-size:12.5px;line-height:1.5}
.address strong{color:var(--green);font-weight:700}
.web{display:flex;align-items:center;gap:8px;color:var(--green);font-weight:700;font-size:13px;margin:10px 0 14px;white-space:nowrap}
.web::before,.web::after{content:"";flex:1;height:2px;background:var(--green)}
.member{display:flex;align-items:center;justify-content:center;gap:12px;margin-top:14px}
.member-badge{width:74px;height:52px;background:#e9ece6;border:1px solid #c9cfc4}
.member-name{font-size:11.5px;line-height:1.3}
.cover-claim{position:absolute;left:0;right:0;top:560px;text-align:center;z-index:3}
.cover-claim small{display:block;font-size:15px;letter-spacing:1px;margin-bottom:4px}
.cover-claim strong{display:block;color:var(--green);font-weight:800;font-size:36px;line-height:1;text-transform:uppercase;letter-spacing:1px}
.ring{position:absolute;border-radius:50%;border:6px solid var(--brown);border-right-color:transparent;border-bottom-color:transparent;transform:rotate(-20deg);z-index:1}
</style>
</head>
<body>
<div class="canvas">

  <!-- Inside spread -->
  <section class="spread spread--inside">
    <div class="panel">
      <svg class="deco deco--top" height="80" viewBox="0 0 380 80"><path d="M0 0H380V36Q190 44 0 70Z" fill="var(--green)"/></svg>
      <span class="band-label">24-STUNDEN SERVICE</span>
      <div class="section" style="padding-top:92px">
        <span class="kicker">Unser</span>
        <h2 class="heading">Leistungsangebot</h2>
        <ul class="checklist">
          <li>24-Stunden Rufbereitschaft</li>
          <li>Häusliche Versorgung</li>
          <li>Qualifiziertes &amp; examiniertes Pflegepersonal</li>
          <li>Verhinderungspflege</li>
          <li>Nachsorge bei Krankenhausbehandlung</li>
          <li>Pflegeberatung nach §37 SGB XI</li>
        </ul>
      </div>
      <div class="section" style="margin-top:22px">
        <span class="kicker">Häusliche</span>
        <h2 class="heading">Grundpflege</h2>
        <ul class="checklist">
          <li>Körperpflege &amp; Hygiene</li>
          <li>Ernährung &amp; Nahrungsaufnahme</li>
          <li>Mobilität, Bewegung &amp; Transfer</li>
        </ul>
      </div>
      <div class="photo photo--pills" role="img" aria-label="Foto: Hände sortieren Tabletten in einer Medikamentenbox" style="left:36px;top:540px;width:210px;height:210px"></div>
      <svg class="deco deco--bottom" height="140" viewBox="0 0 380 140"><path d="M0 40Q120 110 380 120V140H0Z" fill="var(--green-light)"/><path d="M0 80Q160 120 380 126V140H0Z" fill="var(--green)"/></svg>
    </div>

    <div class="panel">
      <div class="section" style="padding-top:40px">
        <span class="kicker">Lindwerk Pflege Brandel</span>
        <h2 class="heading">Pflegeleitbild</h2>
        <ul class="checklist">
          <li>Besserung statt Aufrechterhaltung</li>
          <li>Ambulante vor stationärer Pflege</li>
          <li>Kooperation mit Angehörigen ist uns wichtig</li>
          <li>Eine Vertrauensbasis &amp; Aufrichtigkeit</li>
          <li>Zuverlässigkeit</li>
          <li>Individualität</li>
          <li>Gewährleistung &amp; Qualitätssicherung</li>
          <li>Kulturensensible Pflege</li>
        </ul>
      </div>
      <div class="section" style="margin-top:22px">
        <span class="kicker">Hauswirtschaftliche</span>
        <h2 class="heading">Versorgung</h2>
        <ul class="checklist">
          <li>Einkäufe &amp; Besorgungen</li>
          <li>Reinigung der Wohnung</li>
          <li>Wäsche waschen</li>
        </ul>
      </div>
      <div class="photo photo--hair" role="img" aria-label="Foto: Pflegerin kämmt einer älteren Dame die Haare" style="left:-30px;top:560px;width:200px;height:200px"></div>
      <div class="photo photo--wash" role="img" aria-label="Foto: Arm wird mit einem Waschlappen gewaschen" style="left:170px;top:540px;width:220px;height:220px"></div>
      <svg class="deco deco--bottom" height="90" viewBox="0 0 380 90"><path d="M0 70Q200 80 380 60V90H0Z" fill="var(--green)"/></svg>
    </div>

    <div class="panel">
      <svg class="deco deco--top" height="60" viewBox="0 0 380 60"><path d="M0 0H380V50Q200 20 0 30Z" fill="var(--green)"/></svg>
      <div class="photo photo--hug" role="img" aria-label="Foto: ältere Frau umarmt eine Angehörige" style="left:48px;top:30px;width:284px;height:230px"></div>
      <div class="section" style="padding-top:300px">
        <span class="kicker">Ärztlich verordnete</span>
        <h2 class="heading">Behandlungspflege</h2>
        <ul class="checklist">
          <li>Wundversorgung &amp; Verbandswechsel</li>
          <li>Medikamentengabe- &amp; vorbereitung</li>
          <li>PEG-Versorgung</li>
          <li>Stoma-Versorgung</li>
          <li>Dekubitusbehandlung</li>
          <li>Krankenhausnachsorge</li>
          <li>Katheterpflege</li>
          <li>Blasenspülung</li>
        </ul>
      </div>
      <svg class="deco deco--bottom" height="150" viewBox="0 0 380 150"><path d="M0 80Q220 60 380 0V150H0Z" fill="var(--green-light)"/><path d="M0 90Q220 70 380 14V150H0Z" fill="var(--green)"/></svg>
      <span class="banner-text" style="left:48px;bottom:44px">Kostenlose Beratung</span>
    </div>
  </section>

  <!-- Outside spread -->
  <section class="spread spread--outside">
    <div class="panel">
      <svg class="deco deco--top" height="70" viewBox="0 0 380 70"><path d="M0 0H380V10Q190 20 0 50Z" fill="var(--green)"/></svg>
      <div class="photo photo--hair" role="img" aria-label="Foto: Pflegerin kämmt einer älteren Dame die Haare" style="left:30px;top:56px;width:300px;height:250px"></div>
      <div class="section" style="padding-top:340px">
        <span class="kicker">Immer für Sie da</span>
        <h2 class="heading">Unser Service</h2>
        <ul class="checklist">
          <li>Wir beraten Sie rund um das Thema Pflege</li>
          <li>Hilfe bei der Antragsstellung</li>
          <li>Fahrdienst &amp; Begleitung zu Arztbesuchen &amp; Behördengängen</li>
          <li>Beratung &amp; Hilfe für pflegende Angehörige</li>
          <li>Unser Sprachangebot: Deutsch, Englisch, Russisch</li>
          <li>Pflege &amp; Betreuung von körperbehinderten Menschen, Demenzkranken &amp; MS-Kranken</li>
          <li>Vermittlung von Pflegehilfsmitteln Dritter</li>
        </ul>
      </div>
      <svg class="deco deco--bottom" height="90" viewBox="0 0 380 90"><path d="M0 50Q200 30 380 40V90H0Z" fill="var(--green)"/></svg>
    </div>

    <div class="panel">
      <div class="section" style="padding-top:34px">
        <span class="kicker">Kostenlose</span>
        <h2 class="heading">Beratung</h2>
        <p class="body-copy">Vereinbaren Sie einen kostenlosen, unverbindlichen Beratungstermin:</p>
        <p class="phone">
          <svg width="26" height="26" viewBox="0 0 24 24" aria-hidden="true"><path fill="var(--green)" d="M6.6 10.8a15.1 15.1 0 0 0 6.6 6.6l2.2-2.2a1 1 0 0 1 1-.25 11.4 11.4 0 0 0 3.6.57 1 1 0 0 1 1 1V20a1 1 0 0 1-1 1A17 17 0 0 1 3 4a1 1 0 0 1 1-1h3.5a1 1 0 0 1 1 1c0 1.25.2 2.45.57 3.6a1 1 0 0 1-.25 1Z"/></svg>
          01234 5680 210
        </p>
        <p class="body-copy">Bürozeiten: Montag – Freitag 09:00 – 15:00 Uhr<br>Termine nach Vereinbarung</p>
      </div>
      <div class="section" style="margin-top:30px">
        <p class="brand"><span class="brand-dot"></span>Lindwerk Pflege<span class="brand-sub">Brandel</span></p>
      </div>
      <div class="section" style="margin-top:22px">
        <p class="address"><strong>Lindwerk Pflege Brandel GmbH</strong><br>Ahornweg 12 | 10115 Musterstadt<br>Inhaber: Jonas Brandel<br>info@lindwerk-pflege.de</p>
        <p class="web">www.lindwerk-pflege.de</p>
        <p class="body-copy">Lindwerk Pflege Brandel GmbH ist zugelassen<br>bei allen Kassen und Mitglied im:</p>
        <div class="member">
          <span class="member-badge" role="img" aria-label="Verbandsabzeichen"></span>
          <span class="member-name">Pflegeverband<br>Nordland e. V.</span>
        </div>
      </div>
      <svg class="deco deco--bottom" height="70" viewBox="0 0 380 70"><path d="M0 40Q200 20 380 30V70H0Z" fill="var(--green)"/></svg>
    </div>

    <div class="panel">
      <svg class="deco deco--top" height="60" viewBox="0 0 380 60"><path d="M0 0H380V10Q190 20 0 40Z" fill="var(--green)"/></svg>
      <div class="section" style="padding-top:56px">
        <p class="brand"><span class="brand-dot"></span>Lindwerk Pflege<span class="brand-sub">Brandel</span></p>
      </div>
      <div class="ring" style="left:38px;top:220px;width:304px;height:304px"></div>
      <div class="photo photo--duo" role="img" aria-label="Foto: junge Frau und ältere Dame lächeln gemeinsam" style="left:56px;top:238px;width:268px;height:268px"></div>
      <div class="cover-claim">
        <small>Rund um die Uhr</small>
        <strong>Optimal</strong>
        <strong>Versorgt</strong>
      </div>
      <svg class="deco deco--bottom" height="150" viewBox="0 0 380 150"><path d="M0 110Q200 70 380 20V150H0Z" fill="var(--green-light)"/><path d="M0 120Q220 90 380 40V150H0Z" fill="var(--green)"/></svg>
    </div>
  </section>

</div>
</body>
</html>
```